homepage design for online & live financial management course

homepage logo & required elements can be seen here -
http://kvt-portland.net/Index_new2011

we need a nice design to make it sing, and convert visitors to buyers

we like "Discover Hidden Profits in Your Business — Today!" but don't know how to incorporate it into the design

nice job! thanks for these submissions! keep it up -margaret @kvt/ledger summit (love the more elegant, simple lines of some of these!)

Industry/Entity Type

Financial

Requirements
Must have
• We need to have on the homepage -

- our logo (can not change) "Ledger Summit"
- our tag line (can not change) "Measure. Manage. Succeed."
- our 2-minute introductory video
- 2 options/buttons for visitor's next step: choose Online -or- Live

seen here -

```html
<!DOCTYPE html>
<html lang="en">
<head>
<meta charset="utf-8">
<title>Ledger Summit — Discover Hidden Profits in Your Business</title>
<link rel="stylesheet" href="https://fonts.googleapis.com/css2?family=Arimo:ital,wght@0,400;0,700;1,700&family=Sorts+Mill+Goudy&family=PT+Sans+Narrow:wght@700&display=swap">
<style>
  :root {
    --page-green: #215a3d;
    --panel-green: #1d7a40;
    --bright-green: #3fa535;
    --deep-green: #227a1f;
    --text-green: #3c9a26;
    --headline-green: #1f5e38;
    --body-grey: #8a8a8a;
    --light-grey: #efefef;
    --mid-grey: #b9b9b9;
    --white: #ffffff;
    --black: #111111;
    --footer-text: #d8d8d8;
  }
  * { box-sizing: border-box; margin: 0; padding: 0; }
  html, body { width: 1200px; height: 1001px; overflow: hidden; }
  body { background: var(--page-green); font-family: "Arimo", Arial, sans-serif; position: relative; }
  a { text-decoration: none; }

  .brand { position: absolute; left: 68px; top: 68px; }
  .brand__name { color: var(--white); font-family: "Arimo", Arial, sans-serif; font-weight: 700; font-size: 28px; line-height: 32px; white-space: nowrap; }

  .main-nav { position: absolute; top: 96px; left: 0; width: 1200px; height: 41px; }
  .main-nav a { position: absolute; color: var(--white); font-weight: 700; font-size: 16px; top: 12px; transform: translateX(-50%); }
  .main-nav .is-active { left: 523px; top: 0; width: 91px; height: 41px; transform: none; text-align: center; padding-top: 12px; border-radius: 8px 8px 0 0; background: linear-gradient(#5cc24c, var(--bright-green)); }

  .hero { position: absolute; left: 48px; top: 137px; width: 1104px; height: 377px; background: var(--panel-green); border-radius: 10px 10px 0 0; }
  .video { position: absolute; left: 29px; top: 26px; width: 780px; height: 344px; border-radius: 8px; overflow: hidden; background: #000; }
  .video__still { position: absolute; inset: 0 0 29px 0; background: radial-gradient(ellipse at 55% 40%, #a24a3e 0%, #6e3a6a 35%, #3c2548 75%, #26182e 100%); }
  .video__play { position: absolute; left: 346px; top: 138px; width: 92px; height: 58px; border-radius: 10px; background: rgba(20,20,20,0.85); }
  .video__play::after { content: ""; position: absolute; left: 36px; top: 15px; border-left: 24px solid var(--white); border-top: 14px solid transparent; border-bottom: 14px solid transparent; }
  .video__controls { position: absolute; left: 0; bottom: 0; width: 100%; height: 29px; background: linear-gradient(#f4f4f4, #cfcfcf); display: flex; align-items: center; padding: 0 10px; gap: 12px; font-size: 11px; color: #333; }
  .video__track { flex: 1; height: 8px; border-radius: 4px; background: #e7e7e7; border: 1px solid #a8a8a8; position: relative; }
  .video__track::before { content: ""; position: absolute; left: -2px; top: -5px; width: 16px; height: 16px; border-radius: 50%; background: #666; }

  .path-card { position: absolute; left: 833px; width: 250px; height: 161px; border-radius: 14px; overflow: hidden; background: linear-gradient(#4fbb3f, var(--deep-green)); box-shadow: 0 3px 6px rgba(0,0,0,0.35); color: var(--white); text-align: center; }
  .path-card--live { top: 24px; }
  .path-card--online { top: 206px; }
  .path-card__head { height: 66px; background: linear-gradient(#ffffff, #c9c9c9); border-radius: 0 0 50% 50% / 0 0 18px 18px; color: #444; padding-top: 12px; line-height: 20px; }
  .path-card__head span { display: block; font-size: 18px; }
  .path-card__head strong { display: block; font-size: 19px; font-style: italic; font-weight: 700; }
  .path-card__body { padding-top: 16px; font-size: 18px; line-height: 26px; }
  .path-card__body strong { font-size: 24px; }

  .content { position: absolute; left: 48px; top: 514px; width: 1104px; height: 394px; background: var(--white); }
  .content__headline { position: absolute; top: 30px; width: 100%; text-align: center; font-family: "Sorts Mill Goudy", Georgia, serif; font-weight: 400; font-size: 31px; color: var(--headline-green); }
  .content__intro { position: absolute; left: 29px; top: 118px; width: 700px; font-size: 13.5px; line-height: 22px; color: var(--body-grey); }
  .content__intro p + p { margin-top: 16px; }
  .content__intro strong { color: var(--text-green); }

  .actions { position: absolute; top: 248px; left: 0; }
  .action { position: absolute; text-align: center; font-size: 13px; color: var(--body-grey); }
  .action__label { display: block; margin-bottom: 8px; white-space: nowrap; }
  .btn { display: block; height: 30px; line-height: 28px; border-radius: 7px; font-size: 13px; color: #222; border: 1px solid #888; box-shadow: 0 5px 6px rgba(0,0,0,0.12); }
  .btn--cart { background: linear-gradient(#fafafa, #d8d8d8); }
  .btn--learn, .btn--login { background: linear-gradient(#7ad365, #2e9a23); border-color: #226b1c; }

  .office { position: absolute; left: 809px; top: 117px; width: 266px; height: 212px; border-radius: 10px; background: var(--light-grey); overflow: hidden; }
  .office__map { height: 134px; background: linear-gradient(#f1f1f1, #e2e2e2); }
  .office__address { font-style: normal; text-align: center; font-size: 13.5px; line-height: 22px; color: var(--mid-grey); padding-top: 6px; }
  .office__address strong { display: block; }

  .tagline { position: absolute; left: 411px; top: 874px; width: 378px; height: 36px; }
  .tagline__text { position: absolute; inset: 0; text-align: center; line-height: 38px; color: var(--white); font-family: "PT Sans Narrow", "Arial Narrow", sans-serif; font-weight: 700; font-size: 21px; letter-spacing: 0.5px; }

  .site-footer { position: absolute; left: 48px; top: 908px; width: 1104px; height: 45px; background: linear-gradient(#2b2b2b, var(--black)); }
  .site-footer__copy { position: absolute; left: 29px; top: 16px; font-size: 12px; font-weight: 700; color: var(--footer-text); }
  .social { position: absolute; right: 16px; top: 13px; display: flex; gap: 13px; list-style: none; }
  .social li { width: 19px; height: 19px; border-radius: 3px; background: #8d8d8d; }
</style>
</head>
<body>
  <header>
    <div class="brand">
      <span class="brand__name">Ledger Summit</span>
    </div>
    <nav class="main-nav">
      <a class="is-active" href="#">Home</a>
      <a href="#" style="left:740px">About Us</a>
      <a href="#" style="left:922px">Services</a>
      <a href="#" style="left:1100px">Contact</a>
    </nav>
  </header>

  <section class="hero">
    <div class="video">
      <div class="video__still" role="img" aria-label="Introductory video still: course presenter speaking in a studio set"></div>
      <span class="video__play" aria-hidden="true"></span>
      <div class="video__controls">
        <svg width="14" height="14" viewBox="0 0 14 14" aria-hidden="true"><path d="M2 1 L13 7 L2 13 Z" fill="#333"/></svg>
        <svg width="16" height="14" viewBox="0 0 16 14" aria-hidden="true"><path d="M1 5 H5 L9 1 V13 L5 9 H1 Z" fill="#333"/><path d="M11 4 Q14 7 11 10" stroke="#333" fill="none" stroke-width="1.5"/></svg>
        <span>0:00 / 3:05</span>
        <span class="video__track"></span>
        <svg width="20" height="12" viewBox="0 0 20 12" aria-hidden="true"><rect x="0.5" y="0.5" width="19" height="11" rx="3" fill="#ddd" stroke="#888"/><path d="M5 8 L10 3 L15 8 Z" fill="#333"/></svg>
        <svg width="14" height="14" viewBox="0 0 14 14" aria-hidden="true"><path d="M1 5V1H5M9 1H13V5M13 9V13H9M5 13H1V9" stroke="#333" fill="none" stroke-width="2"/></svg>
      </div>
    </div>

    <a class="path-card path-card--live" href="#">
      <div class="path-card__head"><span>LEDGER</span><strong>SUMMIT LIVE</strong></div>
      <div class="path-card__body"><strong>Learn about</strong><br>in-person events</div>
    </a>
    <a class="path-card path-card--online" href="#">
      <div class="path-card__head"><span>LEDGER</span><strong>SUMMIT ONLINE</strong></div>
      <div class="path-card__body"><strong>Instantly</strong> learn how to<br>unlock hidden profits</div>
    </a>
  </section>

  <main class="content">
    <h1 class="content__headline">Discover Hidden Profits in Your Business — Today!</h1>
    <div class="content__intro">
      <p><strong>Ledger Summit University online</strong> is the financial management course that will give you the tools and confidence to manage your business by the numbers.</p>
      <p>After watching <strong>Ledger Summit University online</strong> and working our case studies, you'll never again feel intimidated by your banker or CPA — and you'll never look at your business the same again.</p>
    </div>
    <div class="actions">
      <div class="action" style="left:165px;width:102px"><span class="action__label">Ready to order?</span><a class="btn btn--cart" href="#">Add to Cart</a></div>
      <div class="action" style="left:322px;width:120px"><span class="action__label">Want to learn more?</span><a class="btn btn--learn" href="#">Learn More</a></div>
      <div class="action" style="left:487px;width:120px"><span class="action__label">Already enrolled?</span><a class="btn btn--login" href="#">Log on</a></div>
    </div>
    <aside class="office">
      <div class="office__map" role="img" aria-label="World map showing the office location"></div>
      <address class="office__address">
        <strong>Keystone Venture Training, Inc.</strong>
        450 Harbor Lane&nbsp;&nbsp;Suite 210<br>
        Portland, OR&nbsp;&nbsp;97204
      </address>
    </aside>
  </main>

  <div class="tagline">
    <svg width="378" height="36" viewBox="0 0 378 36" aria-hidden="true"><path d="M0 36 C18 36 20 0 42 0 H336 C358 0 360 36 378 36 Z" fill="#151515"/></svg>
    <p class="tagline__text">MEASURE. MANAGE. SUCCEED.</p>
  </div>

  <footer class="site-footer">
    <p class="site-footer__copy">© 2010 Keystone Venture Training</p>
    <ul class="social" aria-label="Social links">
      <li aria-label="Social link 1"></li>
      <li aria-label="Social link 2"></li>
      <li aria-label="Social link 3"></li>
      <li aria-label="Social link 4"></li>
      <li aria-label="Social link 5"></li>
      <li aria-label="Social link 6"></li>
    </ul>
  </footer>
</body>
</html>
```